Social Media designs (LinkedIn banner, LinkedIn posts, Instagram)

Hello designers!
We are looking to create some more concepts for our social media identity for a search firm (recruitment company)
I have attached a "brand toolkit" that shows our brand, logo, colour scheme to guide you with regards to colours and identiy.

You will see in the brand toolkit there are some examples of;
- A LinkedIn banner for the company (page 23)
- Social Media posts for LinkedIn and Instagram (page 21)

What we are looking for...

We don't really like the current LinkedIn banner ideas. We would like to see more concepts that look more aesthetically pleasing - the current ideas look quite dull.

We DO like the social media post concepts but we would like to have more templates/options that we can use (similar themes)

We welcome submissions for Social Media designs that we can use with our company branding. Thank you for your work in advance!

```html
<!DOCTYPE html>
<html lang="en">
<head>
<meta charset="utf-8">
<title>Harlow Reid – Case Manager Enhanced Due Dilligence</title>
<link rel="stylesheet" href="https://fonts.googleapis.com/css2?family=Figtree:wght@500;600&display=swap">
<style>
  :root {
    --brand-green: #4a8a6d;
    --brand-ink: #1d3a2e;
    --text-black: #111111;
    --bg-light: #f2f2f2;
    --bg-mid: #e3e3e4;
    --photo-dark: #1c2328;
    --photo-mid: #3a3f44;
    --photo-warm: #8a6a4a;
  }
  html, body {
    margin: 0;
    padding: 0;
    overflow: hidden;
  }
  .banner {
    position: relative;
    width: 1200px;
    height: 300px;
    overflow: hidden;
    font-family: "Figtree", sans-serif;
    background:
      radial-gradient(ellipse 420px 120px at 300px 90px, rgba(255,255,255,0.9), transparent 70%),
      radial-gradient(ellipse 500px 140px at 600px 240px, rgba(255,255,255,0.8), transparent 70%),
      linear-gradient(160deg, var(--bg-light) 0%, var(--bg-mid) 35%, #f6f6f6 55%, var(--bg-mid) 80%, var(--bg-light) 100%);
  }
  .brand {
    position: absolute;
    left: 39px;
    top: 21px;
    display: flex;
    align-items: center;
    gap: 29px;
  }
  .brand-square {
    width: 84px;
    height: 84px;
    background: var(--brand-green);
  }
  .brand-name {
    margin: 0;
    font-size: 40px;
    font-weight: 600;
    line-height: 42px;
    color: var(--brand-ink);
  }
  .headline {
    position: absolute;
    left: 40px;
    top: 158px;
    margin: 0;
    font-size: 35px;
    font-weight: 500;
    line-height: 47px;
    color: var(--text-black);
    letter-spacing: 0.2px;
  }
  .headline .accent {
    color: var(--brand-green);
  }
  .photo-collage {
    position: absolute;
    left: 0;
    top: 0;
    width: 1200px;
    height: 300px;
  }
  .code-mark {
    position: absolute;
    right: 14px;
    bottom: 6px;
    font-size: 7px;
    color: #777;
  }
</style>
</head>
<body>
  <div class="banner">
    <div class="brand">
      <div class="brand-square"></div>
      <p class="brand-name">Harlow<br>Reid</p>
    </div>

    <h1 class="headline"><span class="accent">Case Manager</span> Enhanced<br>Due Dilligence</h1>

    <svg class="photo-collage" viewBox="0 0 1584 396" role="img" aria-label="Photo of an elevated city train on curved tracks between dark buildings, cut into rounded shapes">
      <defs>
        <linearGradient id="photoTone" x1="0" y1="0" x2="1" y2="1">
          <stop offset="0" stop-color="#2b3338"/>
          <stop offset="0.45" stop-color="#1c2328"/>
          <stop offset="0.7" stop-color="#4a4238"/>
          <stop offset="1" stop-color="#2a2622"/>
        </linearGradient>
      </defs>
      <g fill="url(#photoTone)">
        <path d="M905 25 A150 150 0 0 1 1050 175 A150 150 0 0 1 940 262 L905 262 Z"/>
        <rect x="905" y="265" width="35" height="92"/>
        <path d="M1135 0 H1350 V396 H1020 A150 150 0 0 0 1050 300 V175 A150 150 0 0 0 1135 40 Z"/>
        <path d="M1440 0 H1584 V200 A50 50 0 0 0 1550 250 V396 H1350 V290 H1440 Z"/>
      </g>
      <rect x="1243" y="0" width="2" height="396" fill="#d8d8d8"/>
    </svg>

    <span class="code-mark">C 25</span>
  </div>
</body>
</html>
```